Wordpress Design Project (Brantvik)

We need a wordpress design for an established auction and real estate company based in Minnesota. The winning design will incorporate the colors of logo (red white and black) creatively in a very professional and clean layout. Client mentions liking the site http://www.dornwellsales.example/ and http://www.tarpliconauction.example/ as a general idea for what they like.

Industry/Entity Type

Real Estate

Requirements
Must have
• Navigation:
1) Home - will have auction list, no text
2) Upcoming Auctions
3) Online Auctions
4) Real Estate
5) Auction Gallery
6) For Sale
7) About Us
8) Contact Us

Sidebar widget will include:
- email signup
- asset for sale fader (seen in Featured Listings at http://www.tarpliconauction.example/)
- Slideshow - initial image attached
- Video widget (image attached)
- social media icons for Youtube, Facebook, Twitter, LinkedIn and RSS feed
- testimonials

Footer will have smaller logo and contact info
Nice to have
• Nice to Have:
- use of drop-down menu design for 'About Us'
1) About Brantvik
2) Testimonials

```html
<!DOCTYPE html>
<html lang="en">
<head>
<meta charset="utf-8">
<title>Brantvik Auction &amp; Real Estate Services</title>
<link href="https://fonts.googleapis.com/css2?family=Arimo:ital,wght@0,400;0,700;1,400;1,700&family=Roboto+Condensed:wght@700&display=swap" rel="stylesheet">
<style>
:root{
  --red:#8c0b10;
  --red-text:#8e0b12;
  --dark:#2c2c2c;
  --ink:#222;
  --grey-text:#666;
  --muted:#8a8a8a;
  --page-bg:#ececec;
  --panel-line:#e2e2e2;
  --white:#fff;
}
*{margin:0;padding:0;box-sizing:border-box}
html,body{width:916px;height:1200px;overflow:hidden}
body{background:var(--page-bg);font-family:"Arimo",Arial,sans-serif;color:var(--ink);position:relative}
.page{position:absolute;left:60px;top:33px;width:766px;height:1114px;background:var(--white);box-shadow:0 0 3px rgba(0,0,0,.08);overflow:hidden}
.abs{position:absolute}

.header{left:0;top:0;width:766px;height:99px;background:linear-gradient(#fff,#f3f3f3)}
.brand{left:17px;top:22px;display:flex;align-items:center;gap:8px}
.brand-mark{width:22px;height:22px;background:var(--red)}
.brand-name{font-weight:700;font-size:34px;color:var(--red);letter-spacing:1px}
.brand-phone{left:47px;top:64px;font-size:11px;font-weight:700;color:var(--red)}
.tagline{left:220px;top:24px;width:280px;text-align:center;font-style:italic;font-weight:700;font-size:16px;color:#9a9a9a;line-height:26px}
.cell{left:550px;top:40px;font-style:italic;font-weight:700;font-size:22px;color:#444}
.cell span{color:var(--red)}

.nav{left:0;top:99px;width:766px;height:37px;background:var(--red);display:flex;justify-content:space-between}
.nav a{flex:none;white-space:nowrap;color:var(--white);text-decoration:none;font-weight:700;font-size:12px;line-height:37px;padding:0 12px}
.nav a.active{background:#1e1e1e}
.dropdown{left:69px;top:136px;width:152px;background:rgba(25,25,25,.92);padding:4px 0;z-index:3}
.dropdown a{display:block;color:var(--white);text-decoration:none;font-weight:700;font-size:11px;padding:7px 15px}

.hero-photo{left:16px;top:149px;width:447px;height:308px;background:linear-gradient(135deg,#4a8a38,#6b5a48 45%,#3f7a30 70%,#8a3a2a)}
.listing{left:463px;top:149px;width:288px;height:308px;background:var(--dark);text-align:center;color:var(--white)}
.listing h2{font-style:italic;font-size:22px;margin-top:12px}
.listing-photo{margin:12px auto 0;width:225px;height:136px;background:linear-gradient(#6c9ad6,#b9c9d8 50%,#7fa35a)}
.listing .price{font-style:italic;font-weight:700;font-size:21px;line-height:26px;margin-top:12px}
.listing .desc{font-style:italic;font-weight:700;font-size:11px;color:#999;line-height:15px;margin-top:10px}

.content{left:16px;top:471px;width:735px;height:423px;border:1px solid var(--panel-line);border-radius:4px;background:#fafafa}
.box{border:1px solid var(--panel-line);border-radius:5px;background:var(--white)}
.welcome{left:29px;top:485px;width:475px;height:191px}
.welcome h1{position:absolute;left:16px;top:16px;font-size:22px;color:#555}
.welcome h1 span,.upcoming h1 span{color:var(--red-text)}
.welcome p{position:absolute;left:16px;top:52px;width:330px;font-size:9px;line-height:11px;color:var(--grey-text);text-align:justify}
.portrait{left:362px;top:52px;width:92px;height:109px;background:linear-gradient(#c8b6a8,#2a2c3a 70%)}

.upcoming{left:29px;top:687px;width:475px;height:188px}
.upcoming h1{position:absolute;left:18px;top:16px;font-size:21px;color:#555}
.auction-photo{left:18px;top:57px;width:129px;height:108px;background:linear-gradient(#8a9a7a,#b02530 55%,#6a8a40)}
.auction-title{left:196px;top:54px;font-weight:700;font-size:12px;line-height:15px;color:var(--red-text)}
.auction-date{left:196px;top:99px;font-weight:700;font-size:11.5px}
.auction-info{left:196px;top:117px;font-size:9.5px;line-height:15px;color:var(--grey-text)}

.video{left:519px;top:485px;width:222px;height:172px}
.video-frame{left:12px;top:12px;width:197px;height:148px;background:linear-gradient(#1a1a1a 0 16px,#f0eeee 16px,#e8dede 85%,#111 85%)}
.play{left:84px;top:56px;width:30px;height:30px;border-radius:50%;background:rgba(255,255,255,.75)}
.play:after{content:"";position:absolute;left:11px;top:8px;border-left:11px solid #555;border-top:7px solid transparent;border-bottom:7px solid transparent}

.promo{left:519px;top:668px;width:222px;height:126px;padding:27px 14px 0;text-align:center;font-weight:700;font-size:9px;line-height:12px;color:var(--grey-text)}
.social{left:519px;top:812px;width:222px;height:62px;display:flex;justify-content:center;gap:14px;align-items:center}
.social span{width:22px;height:22px;border-radius:3px}

.footer-head{font-family:"Roboto Condensed",Arial,sans-serif;font-weight:700;font-size:14px;color:#333;text-transform:uppercase}
.nice{left:23px;top:917px}
.nice ul{list-style:none;margin-top:14px}
.nice li{font-size:9.5px;color:#444;line-height:21px}
.nice li:before{content:"\2192";color:#777;margin-right:9px;font-size:9px}
.contact{left:220px;top:917px}
.contact p{margin-top:14px;font-size:9.5px;line-height:15.5px;color:#444}
.contact b{color:#333}
.contact .email{color:var(--red-text);font-weight:700}
.footer-brand{left:500px;top:970px;width:250px;display:flex;align-items:center;gap:10px}
.footer-brand .mark{flex:none;width:32px;height:32px;background:#9a9a9a}
.footer-brand .name{white-space:nowrap;font-weight:700;font-size:42px;color:#9a9a9a}

.copyright{left:0;top:1072px;width:766px;height:42px;background:#e9e9e9;text-align:center;font-size:9px;color:#888;line-height:42px}
</style>
</head>
<body>
<div class="page">
  <header class="header abs">
    <div class="brand abs"><span class="brand-mark"></span><span class="brand-name">Brantvik</span></div>
    <div class="brand-phone abs">320-555-0143</div>
    <div class="tagline abs">It's Your Auction &amp; Your Money.....<br>Don't sell it short, call Brantvik !</div>
    <div class="cell abs">Cell: <span>320-555-0186</span></div>
  </header>

  <nav class="nav abs">
    <a href="#">Home</a>
    <a href="#" class="active">About Us</a>
    <a href="#">Online Auctions</a>
    <a href="#">Real Estate</a>
    <a href="#">Auction Gallery</a>
    <a href="#">For Sale</a>
    <a href="#">Upcoming Auctions</a>
    <a href="#">Contact Us</a>
  </nav>
  <div class="dropdown abs">
    <a href="#">About Brantvik</a>
    <a href="#">Testimonials</a>
  </div>

  <div class="hero-photo abs" role="img" aria-label="Crowd of bidders among rows of farm tractors at an outdoor auction"></div>
  <aside class="listing abs">
    <h2>Elsa Norgaard</h2>
    <div class="listing-photo" role="img" aria-label="Single-storey house with attached garage and driveway"></div>
    <div class="price">*Price Reduced<br>$165,000*</div>
    <div class="desc">3 Bedroom, 2 Bath House Located<br>on Linden Ct in Halvor, MN</div>
  </aside>

  <div class="content abs"></div>

  <section class="welcome box abs">
    <h1>Welcome to <span>Brantvik!</span></h1>
    <p>Lorem Ipsum is simply dummy text of the printing and typesetting industry. Lorem Ipsum has been the industry's standard dummy text ever since the 1500s, when an unknown printer took a galley of type and scrambled it to make a type specimenLorem Ipsum is simply dummy text of the printing and typesetting industry. Lorem Ipsum has been the industry's standard dummy text ever since the 1500s, when an unknown printer took a galley of type and scrambled it to make a type specimenLorem Ipsum is simply dummy text of the print.ing and typesetting industry. Lorem Ipsum has been the industry's standard dummy text ever since the 1500s, when an unknown printer took a galley of type and scrambled it to make a type specimenLorem Ipsum is simply</p>
    <div class="portrait abs" role="img" aria-label="Portrait of the auctioneer in a suit"></div>
  </section>

  <section class="upcoming box abs">
    <h1>UPCOMING <span>AUCTIONS</span></h1>
    <div class="auction-photo abs" role="img" aria-label="Red cars parked on grass at the auction site"></div>
    <div class="auction-title abs">Oskar Lindqvist Estate Auction<br>*Sale Bill and More Photo's Coming Soon!*</div>
    <div class="auction-date abs">Friday, June 28, 2013 - 10:00 AM</div>
    <div class="auction-info abs">418 Prairie Ave<br>Tessdale, MN<br>Building Site, Wood Working Equipment,<br>Tools, Lawn Mower, Car, Household, Collectibles</div>
  </section>

  <div class="video box abs">
    <div class="video-frame abs" role="img" aria-label="Bidder tutorial video preview">
      <div class="play abs"></div>
    </div>
  </div>

  <div class="promo box abs">Lorem Ipsum is simply dummy text of the printing and typesetting industry. Lorem Ipsum has been the industry's standard dummy text ever since the 1500s, when an unknown printer took a galley of type and scrambled it to make a type specimen</div>

  <div class="social box abs" aria-label="Social media links">
    <span style="background:#c4302b"></span>
    <span style="background:#0e76a8"></span>
    <span style="background:#3b5998"></span>
    <span style="background:#ee802f"></span>
    <span style="background:#2a9fd6"></span>
  </div>

  <div class="nice abs">
    <div class="footer-head">Nice to have</div>
    <ul>
      <li>Home</li><li>About Us</li><li>Services</li><li>FAQ</li><li>Contact Us</li>
    </ul>
  </div>

  <div class="contact abs">
    <div class="footer-head">Contact info</div>
    <p><b>Brantvik Auctions &amp; Real Estate Service</b><br>27 Birch Street East<br>Halvor, MN&nbsp; 56000<br><span class="email">Email: info@brantvik.example</span><br><b>Office:</b> 320-555-0143, <b>Cell:</b> 320-555-0186<br><b>Fax:</b> 320-555-0177</p>
  </div>

  <div class="footer-brand abs"><span class="mark"></span><span class="name">Brantvik</span></div>

  <footer class="copyright abs">© 2013 www.brantvik.example All rights reserved.</footer>
</div>
</body>
</html>
```